Dental Office Business Card

We need a business card for our pediatric dentistry office.
On one side the design needs to contain the following:
our logo (attached)
Vento Pediatric Grins
Soraya Kadbelani, DDS
Board Certified Pediatric Dentist
Tel: (555) 318-2747)
Fax: (555) 264-8031
Email: info@ventopediatricgrins.example
Web: www.ventopediatricgrins.example
Address: 41 Brindle Ave, Suite 208, Wellesley, MA 02099

On the other side of the card, the design needs to have an appointment reminder (date and time as well as day of the week) similar to the design attached (no need for appointment reason “For”)

```html
<!DOCTYPE html>
<html lang="en">
<head>
<meta charset="utf-8">
<title>Vento Pediatric Grins – Business Card</title>
<link href="https://fonts.googleapis.com/css2?family=Montserrat:wght@500;600&family=Nunito:wght@400;500;700&family=Playfair+Display:ital,wght@1,400;1,500&family=Roboto:wght@400&display=swap" rel="stylesheet">
<style>
  :root {
    --mint: #a8d6a8;
    --ink: #1e1c1d;
    --text: #4a4a4a;
    --paper: #ffffff;
    --backdrop: #8c8c8c;
  }
  * { margin: 0; padding: 0; box-sizing: border-box; }
  html, body { width: 1188px; height: 1200px; overflow: hidden; }
  body { background: var(--backdrop); position: relative; }

  .card {
    position: absolute; left: 245px; width: 696px; height: 386px;
    background: var(--paper); overflow: hidden;
  }
  .card--front { top: 159px; }
  .card--back { top: 627px; }

  /* Front */
  .brand-panel {
    position: absolute; left: 0; top: 0; width: 221px; height: 100%;
    background: var(--mint); border-right: 3px solid var(--ink);
  }
  .brand-dot {
    position: absolute; left: 100px; top: 58px; width: 80px; height: 80px;
    border-radius: 50%; background: var(--paper);
  }
  .brand-name__main,
  .brand-name__sub {
    position: absolute; bottom: 54px;
    writing-mode: vertical-rl; white-space: nowrap;
    font-family: "Nunito", sans-serif; font-weight: 700; color: var(--ink); line-height: 1;
  }
  .brand-name__main { left: 92px; font-size: 64px; }
  .brand-name__sub { left: 56px; font-size: 26px; letter-spacing: 0.02em; }

  .details { position: absolute; left: 265px; top: 58px; }
  .details__name {
    font-family: "Nunito", sans-serif; font-weight: 700; font-size: 27px;
    color: var(--ink); line-height: 1;
  }
  .details__title {
    font-family: "Montserrat", sans-serif; font-weight: 500; font-size: 19.5px;
    color: var(--mint); margin-top: 5px; letter-spacing: 0.01em;
  }
  .details__address {
    font-family: "Roboto", sans-serif; font-size: 20px; color: var(--text);
    line-height: 26px; margin-top: 48px;
  }
  .contact-list { list-style: none; margin-top: 15px; }
  .contact-list li {
    font-family: "Roboto", sans-serif; font-size: 20px; color: var(--text);
    display: flex; align-items: center; height: 26px;
  }
  .contact-list svg { width: 18px; height: 18px; margin-right: 10px; fill: var(--mint); flex: none; }
  .accent { color: var(--mint); }

  /* Back */
  .reminder-head { position: absolute; top: 70px; width: 100%; text-align: center; }
  .reminder-head__title {
    font-family: "Montserrat", sans-serif; font-weight: 600; font-size: 42px;
    letter-spacing: 0.2em; color: var(--ink); line-height: 1; padding-left: 0.2em;
  }
  .reminder-head__sub {
    font-family: "Playfair Display", serif; font-style: italic; font-size: 36px;
    letter-spacing: 0.12em; color: var(--ink); margin-top: 4px;
  }
  .fields {
    position: absolute; left: 55px; top: 220px; display: flex; align-items: flex-end;
    font-family: "Montserrat", sans-serif; font-weight: 500; font-size: 22px; color: var(--ink);
  }
  .fields__line { display: inline-block; border-bottom: 1.5px solid var(--ink); height: 1px; margin: 0 10px 5px 6px; }
  .fields__ampm { font-family: "Playfair Display", serif; font-style: italic; font-size: 24px; letter-spacing: 0.04em; }
  .weekdays {
    position: absolute; left: 55px; right: 55px; top: 278px; display: flex; justify-content: space-between;
    list-style: none; font-family: "Playfair Display", serif; font-style: italic; font-size: 24px; color: var(--ink);
  }
  .weekdays li { display: flex; align-items: center; }
  .weekdays li::before {
    content: ""; width: 20px; height: 20px; border: 1.5px solid var(--ink); margin-right: 12px;
  }
  .back-footer {
    position: absolute; left: 0; bottom: 0; width: 100%; height: 42px;
    border-top: 3px solid var(--ink); background: var(--mint);
    display: flex; align-items: center; justify-content: center;
    font-family: "Nunito", sans-serif; font-size: 17px; letter-spacing: 0.08em; color: var(--paper);
  }
  .back-footer strong { font-weight: 500; color: var(--ink); }
</style>
</head>
<body>
  <section class="card card--front">
    <div class="brand-panel">
      <div class="brand-dot"></div>
      <span class="brand-name__main">Vento</span>
      <span class="brand-name__sub">PEDIATRIC GRINS</span>
    </div>
    <div class="details">
      <h1 class="details__name">Soraya Kadbelani, DDS</h1>
      <p class="details__title">Board Certified Pediatric Dentist</p>
      <p class="details__address">41 Brindle Ave, Suite 208,<br>Wellesley, MA 02099</p>
      <ul class="contact-list">
        <li><svg viewBox="0 0 24 24"><path d="M2 9c0-3 4-5 10-5s10 2 10 5v2h-5V9c-1-1-3-1.5-5-1.5S8 8 7 9v2H2z"/><path d="M6 12l2-3h8l2 3v8H6z"/><circle cx="12" cy="15" r="2.5" fill="#fff"/></svg>(555) 318-2747</li>
        <li><svg viewBox="0 0 24 24"><rect x="6" y="2" width="12" height="8"/><rect x="2" y="10" width="20" height="8" rx="1"/><rect x="5" y="19" width="14" height="3"/></svg>(555) 264-8031</li>
        <li><svg viewBox="0 0 24 24"><path d="M2 5h20v3l-10 6L2 8z"/><path d="M2 10l10 6 10-6v9H2z"/></svg>info@ventopediatricgrins.example</li>
        <li><svg viewBox="0 0 24 24"><circle cx="12" cy="12" r="10"/><path d="M8 6c2 1 3 3 2 5s-3 1-3 4M15 4c-1 2 0 4 2 5s3 3 1 6" stroke="#fff" stroke-width="1.5" fill="none"/></svg>www.<span class="accent">ventopediatricgrins</span>.example</li>
      </ul>
    </div>
  </section>

  <section class="card card--back">
    <header class="reminder-head">
      <h2 class="reminder-head__title">APPOINTMENT</h2>
      <p class="reminder-head__sub">Reminder</p>
    </header>
    <div class="fields">
      <span>DATE :</span><span class="fields__line" style="width:190px"></span>
      <span style="margin-left:4px">TIME :</span><span class="fields__line" style="width:100px;margin-left:14px;margin-right:4px"></span>
      <span class="fields__ampm">a.m. p.m.</span>
    </div>
    <ul class="weekdays">
      <li>Mon</li><li>Tue</li><li>Wed</li><li>Thu</li><li>Fri</li><li>Sat</li><li>Sun</li>
    </ul>
    <footer class="back-footer">www.<strong>ventopediatricgrins</strong>.example</footer>
  </section>
</body>
</html>
```